| バナーサイズ |
| 現在のヘッダーデザインにとらわれず、サイトイメージとマッチするような、 オリジナルのヘッダーを作成して下さい。 ■サイズ ヘッダー画像サイズ:横幅1450px、縦幅680px 対象サイト:http://www.vormeta-k.com ■会社(サービス)概要 企業向けのコンサルティングサービス、各種ビジネスサービスを展開しています。 主に中小企業、中堅企業向けのクライアントが対象 ■利用客層 男性メイン 特に、課長/部長等のマネージメントクラス、役員/経営者向け ■最後に ご質問あれば、回答させて頂きます。 一人で複数の応募も問題ございません。 多くの方からの、ご応募をお待ちしています。 |

```html
<!DOCTYPE html>
<html lang="ja">
<head>
<meta charset="UTF-8">
<title>Vormeta Group ヘッダー</title>
<link rel="stylesheet" href="https://fonts.googleapis.com/css2?family=Noto+Sans+JP:wght@400;700;900&family=Noto+Serif+JP:wght@600&family=Tinos:wght@400&display=swap">
<style>
  :root {
    --navy: #0f1f5c;
    --nav-text: #1c2d6b;
    --sky-top: #ffffff;
    --sky-mid: #cfe2f5;
    --sky-blue: #7fb4e6;
    --deep-blue: #3d6fb8;
    --night: #24346e;
    --headline: #ffffff;
    --shadow: rgba(12, 28, 80, 0.75);
  }
  * { margin: 0; padding: 0; box-sizing: border-box; }
  html, body {
    width: 1200px;
    height: 562px;
    overflow: hidden;
    background: var(--sky-top);
  }
  .header {
    position: relative;
    width: 1200px;
    height: 562px;
    overflow: hidden;
    font-family: "Noto Sans JP", sans-serif;
  }
  .hero-scene {
    position: absolute;
    inset: 0;
    background:
      radial-gradient(ellipse 420px 260px at 560px 330px, rgba(255,255,255,0.55), rgba(255,255,255,0) 70%),
      radial-gradient(ellipse 300px 240px at 1080px 420px, rgba(60,90,170,0.45), rgba(60,90,170,0) 70%),
      radial-gradient(ellipse 260px 200px at 120px 470px, rgba(70,110,190,0.45), rgba(70,110,190,0) 70%),
      linear-gradient(180deg, var(--sky-top) 0%, var(--sky-top) 14%, var(--sky-mid) 32%, var(--sky-blue) 60%, var(--deep-blue) 85%, var(--night) 100%);
  }
  .brand {
    position: absolute;
    left: 30px;
    top: 34px;
    display: flex;
    align-items: center;
    gap: 12px;
  }
  .brand-dot {
    width: 22px;
    height: 22px;
    border-radius: 50%;
    background: var(--navy);
  }
  .brand-name {
    font-family: "Tinos", serif;
    font-size: 32px;
    font-weight: 400;
    color: var(--navy);
    letter-spacing: 0.5px;
  }
  .global-nav {
    position: absolute;
    top: 34px;
    left: 340px;
    display: flex;
    gap: 0;
  }
  .global-nav a {
    display: block;
    width: 150px;
    text-align: center;
    font-size: 14px;
    color: var(--nav-text);
    text-decoration: none;
    letter-spacing: 0.5px;
  }
  .headline {
    position: absolute;
    top: 288px;
    left: 0;
    width: 1200px;
    text-align: center;
    color: var(--headline);
    font-family: "Noto Sans JP", sans-serif;
    font-weight: 700;
    font-size: 42px;
    letter-spacing: 4px;
    text-shadow: 0 0 10px var(--shadow), 0 2px 4px var(--shadow);
  }
  .tagline {
    position: absolute;
    top: 362px;
    left: 0;
    width: 1200px;
    text-align: center;
    color: var(--headline);
    font-family: "Noto Serif JP", serif;
    font-weight: 600;
    font-size: 21px;
    letter-spacing: 1px;
    text-shadow: 0 0 6px var(--shadow), 0 1px 3px var(--shadow);
  }
</style>
</head>
<body>
  <header class="header">
    <div class="hero-scene" role="img" aria-label="青く霞む都市の夜景と空に重なる、前へ歩むビジネスパーソンたちのシルエット"></div>

    <div class="brand">
      <span class="brand-dot"></span>
      <span class="brand-name">Vormeta Group</span>
    </div>

    <nav class="global-nav">
      <a href="#">サービス一覧</a>
      <a href="#">お客様の成功事例</a>
      <a href="#">blog</a>
      <a href="#">会社概要</a>
      <a href="#">お問い合わせ</a>
    </nav>

    <h1 class="headline">今を変えて、未来を創る。</h1>
    <p class="tagline">実践型エキスパートが、戦略的事業創造と新産業創出をハンズオンで支援</p>
  </header>
</body>
</html>
```